Weather card for guests at Fenwick’s Beach House

I am looking to have a card designed for my guests who stay over. The card should show the weather for the next day (emoji's), quote of the day, Activities of the day. It's for a beach house so it should be coastal/Beachy themed. The weather should have a high and a low. (I will fill in each card). It should be front and back. It should be a fun project. Think modern farmhouse. The top of each card should say something like Another great Day at 7 Harbor
Updates

If you google "turn down Service letter" or "hotel weather card". It will provide examples

Target Market(s)

Our guests who visit our beach house

Font styles to use
Sans Serif

Colors
0054AA
0677BA
7BADD7
CADEEF
E8F1F8

Requirements
Must have
• weather options, quote of the day, activity for the day
Nice to have
• Sand, seashells, seagulls
Should not have
• Should not be too busy and not childish

```html
<!DOCTYPE html>
<html lang="en">
<head>
<meta charset="utf-8">
<title>Weather Card – Fenwick’s Beach House</title>
<link rel="stylesheet" href="https://fonts.googleapis.com/css2?family=Montserrat:wght@300;400&family=Alex+Brush&display=swap">
<style>
  :root {
    --page: #ffffff;
    --card: #f8f5f2;
    --card-edge: #c9c6c3;
    --ink: #555555;
    --rule: #bdbab7;
    --shadow: rgba(0, 0, 0, 0.18);
  }
  * { margin: 0; padding: 0; box-sizing: border-box; }
  html, body {
    width: 1200px;
    height: 1000px;
    overflow: hidden;
    background: var(--page);
  }
  body {
    position: relative;
    font-family: "Montserrat", sans-serif;
    font-weight: 300;
    color: var(--ink);
  }
  h2 { font-weight: 300; }
  .card {
    position: absolute;
    left: 261px;
    width: 683px;
    height: 488px;
    background: var(--card);
    border: 1px solid var(--card-edge);
    box-shadow: 5px 5px 6px var(--shadow);
    overflow: hidden;
  }
  .card--front { top: 7px; }
  .card--back { top: 506px; }
  .label {
    position: absolute;
    white-space: nowrap;
    letter-spacing: 0.02em;
    line-height: 1;
    font-weight: 300;
  }
  .greeting {
    left: 28px;
    top: 42px;
    font-size: 28px;
    letter-spacing: 0.03em;
  }
  .place-name {
    position: absolute;
    right: 24px;
    top: 14px;
    font-family: "Alex Brush", cursive;
    font-size: 68px;
    line-height: 1;
    color: var(--ink);
    white-space: nowrap;
    word-spacing: 0.12em;
  }
  .rule-h {
    position: absolute;
    left: 26px;
    width: 637px;
    height: 2px;
    background: var(--rule);
  }
  .rule-v {
    position: absolute;
    left: 316px;
    top: 99px;
    width: 1px;
    height: 370px;
    background: var(--rule);
  }
  .section-title { font-size: 22px; transform: translateX(-50%); }
  .weather-title { left: 160px; top: 132px; }
  .quote-title { left: 496px; top: 132px; }
  .temp-label { font-size: 16px; top: 188px; transform: translateX(-50%); }
  .temp-high { left: 85px; }
  .temp-low { left: 235px; }
  .forecast-title { left: 152px; top: 392px; font-size: 17px; transform: translateX(-50%); }
  .forecast-icons {
    position: absolute;
    left: 34px;
    top: 428px;
  }
  .activities-title {
    left: 31px;
    top: 36px;
    font-size: 28px;
    letter-spacing: 0.03em;
  }
</style>
</head>
<body>

<section class="card card--front">
  <p class="label greeting">ANOTHER GREAT DAY AT</p>
  <p class="place-name">7 Harbor</p>
  <div class="rule-h" style="top:97px"></div>
  <div class="rule-v"></div>

  <h2 class="label section-title weather-title">WEATHER TODAY</h2>
  <p class="label temp-label temp-high">HIGH</p>
  <p class="label temp-label temp-low">LOW</p>

  <h2 class="label section-title quote-title">QUOTE OF THE DAY</h2>

  <p class="label forecast-title">TOMORROW’S FORECAST</p>
  <svg class="forecast-icons" width="240" height="40" viewBox="0 0 240 40" aria-label="Forecast options: sunny, partly cloudy, cloudy, rainy, windy">
    <g fill="#555" stroke="#555">
      <g transform="translate(17,16)">
        <circle r="8" stroke="none"/>
        <circle r="4" fill="#f8f5f2" stroke="none"/>
        <g stroke-width="2.6" stroke-linecap="round">
          <line x1="0" y1="-10" x2="0" y2="-13"/><line x1="0" y1="10" x2="0" y2="13"/>
          <line x1="-10" y1="0" x2="-13" y2="0"/><line x1="10" y1="0" x2="13" y2="0"/>
          <line x1="7" y1="7" x2="9.2" y2="9.2"/><line x1="-7" y1="-7" x2="-9.2" y2="-9.2"/>
          <line x1="7" y1="-7" x2="9.2" y2="-9.2"/><line x1="-7" y1="7" x2="-9.2" y2="9.2"/>
        </g>
      </g>
      <g transform="translate(66,16)">
        <circle cx="6" cy="-5" r="5" stroke="none"/>
        <g stroke-width="1.8" stroke-linecap="round">
          <line x1="6" y1="-13" x2="6" y2="-15"/><line x1="14" y1="-5" x2="16" y2="-5"/>
          <line x1="12" y1="-11" x2="13.5" y2="-12.5"/><line x1="0" y1="-11" x2="-1.5" y2="-12.5"/>
        </g>
        <path stroke="#f8f5f2" stroke-width="1.5" d="M-16 13 h30 a5 5 0 0 0 0-10 a7 7 0 0 0-13-4 a6 6 0 0 0-11 3 a5.5 5.5 0 0 0-6 11z"/>
      </g>
      <path stroke="none" d="M102 31 h27 a5 5 0 0 0 0-10 a8 8 0 0 0-15-4 a6 6 0 0 0-10 3 a5.5 5.5 0 0 0-2 11z"/>
      <g>
        <path stroke="none" d="M155 27 h26 a5 5 0 0 0 0-10 a8 8 0 0 0-15-4 a6 6 0 0 0-10 3 a5.5 5.5 0 0 0-1 11z"/>
        <g stroke-width="1.8" stroke-linecap="round">
          <line x1="160" y1="30" x2="160" y2="37"/><line x1="165" y1="30" x2="165" y2="39"/>
          <line x1="170" y1="30" x2="170" y2="37"/><line x1="175" y1="30" x2="175" y2="35"/>
        </g>
      </g>
      <g fill="none" stroke-width="1.8" stroke-linecap="round">
        <path d="M204 21 h18 a4 4 0 1 0-4-4"/>
        <path d="M204 26 h24 a4 4 0 1 1-4 4"/>
        <path d="M207 31 h10"/>
      </g>
    </g>
  </svg>
</section>

<section class="card card--back">
  <h2 class="label activities-title">TODAY’S ACTIVITIES:</h2>
  <div class="rule-h" style="top:83px"></div>
</section>

</body>
</html>
```